ATM Website-Great Opportunity for Portability

Hey We need YOU to help us make our ATM (Automatic Teller Machine)Website!!) We are a million dollar business that will look great on your portfolio! Our Name is "CORNER CASH POINT"
Previous ATM business (now sold) was www.cashbrivo.com.au (site being pulled down so look at it fast!)
The winner will get the same package that we will giving to the winner of our other project! (worth over $9,000)
http://jobs.pixelvorn.com/job.aspx?id=4827
**we are making a series of sites/applications Winners will be solo invited to work on all upcoming projects of that catigory**
***we are also looking for Outstanding freelance guys to work with on all future projects***
Main Points!!
1: one main page (that is not a blog!)
2: Then the Theme!
3: I don't want it to look like a word-press
I.e like this guys Word press http://www.trasqueld.com/
See how he has one main page then the rest are WP Theme :)
Key points to the Home Page!
See attached pic for the menu's needed and the call now key.
Main page needs to have
1. Clean, uncluttered, and follow the feel of our LOGO (attached) Be creative but simplistic with the page. Round curves are good)
2. Large hero images of happy poeple in the community but not looking too stocky or contrived - natural smiles, natural expressions, With Image of OUR ATM on the page!
3. Easy navigation
4: (3 big buttons like on our competitors site
(http://www.brightfundpoint.com.au/) With the titles
(get an ATM (and beside it "for your business")
(Own an ATM (increase your investment Portfolio)
(Latest ATM (See an ATM in action)
For the Theme Page,
It must flow on from the main menu but have a bread crum trail on the page of all the sub links somewhere on the left of the page (or somewhere else that might look better.
Theme page should have a Call now or email now option!! If you can fit in 2 without it looking cluttered that would be good.
I will attach our brochures so you can get a feel of our product.
Also you should be able to extract images from our brochure using GLEMBRA DOC TOOL or similar PDF editor if needed!!
logo attached and also found at www.cornercashpoint.com.au
Good Fonts to use!
Helvetica Neue LT (bold thin ect)
Helvetica Neue LT Com
Target Market(s)
Business Owners and Investors
Industry/Entity Type
Investment
Requirements
Must have
- The Call now Features in the attached file, Clean layout
Should not have
- Should not look like stock photo's and a cheap website or a template...

```html
<!DOCTYPE html>
<html lang="en">
<head>
<meta charset="utf-8">
<title>Corner Cash Point</title>
<link href="https://fonts.googleapis.com/css2?family=Arimo:wght@400;700&family=Roboto+Condensed:wght@400;700&display=swap" rel="stylesheet">
<style>
:root{
  --lime:#8cc63f;
  --lime-dark:#5a9a1c;
  --green-text:#2f8a1c;
  --green-deep:#1d6a0e;
  --cream:#f4f0d6;
  --red:#e8120f;
  --grey-text:#4a4a4a;
  --page:#f2f2f2;
}
*{box-sizing:border-box;margin:0;padding:0}
html,body{width:1200px;height:779px;overflow:hidden}
body{position:relative;background:var(--page);font-family:"Arimo",Arial,sans-serif}
.top-band{position:absolute;left:0;top:0;width:1200px;height:50px;background:linear-gradient(180deg,#9fd13a,#c3e25a 60%,#a9d43f)}
.header{position:absolute;left:0;top:50px;width:1200px;height:124px;background:linear-gradient(180deg,#fff,#f3f3f3)}
.brand{position:absolute;left:190px;top:58px;display:flex;align-items:center;gap:13px}
.brand-mark{width:68px;height:68px;border-radius:50%;background:var(--lime)}
.brand-name{font-size:15px;color:var(--grey-text);letter-spacing:.3px;margin-top:10px}
.search{position:absolute;left:842px;top:73px;width:168px;height:26px;background:var(--cream);border:1px solid #e2ddb9;font-size:12px;color:#555;padding:6px 0 0 21px}
.search svg{position:absolute;left:2px;top:5px}
.search-btn{position:absolute;left:1016px;top:75px}
.nav{position:absolute;left:0;top:141px;width:1200px;height:22px;font-family:"Roboto Condensed","Arial Narrow",sans-serif;font-size:14.5px;color:#333;list-style:none}
.nav li{position:absolute;top:0;height:22px;line-height:22px;white-space:nowrap}
.nav .active{background:var(--lime);color:#fff;border-radius:2px;width:64px;text-align:center}
.nav-rule{position:absolute;left:0;top:173px;width:1200px;height:3px;background:var(--lime)}
.main{position:absolute;left:0;top:176px;width:1200px;height:484px;background:radial-gradient(ellipse at 45% 35%,#ffffff,#f0f0f0 60%,#dcdcdc)}
.atm-art{position:absolute;left:192px;top:194px;width:162px;height:330px;border-radius:40px 8px 4px 4px;
  background:linear-gradient(90deg,#2f9a3c 0%,#4fb04a 45%,#9aa3a4 52%,#c9cfcf 70%,#8e9596 100%);
  -webkit-mask-image:linear-gradient(180deg,#000 80%,transparent);mask-image:linear-gradient(180deg,#000 80%,transparent)}
.hero-text{position:absolute;left:395px;top:264px;width:360px;font-size:28.5px;line-height:35.5px;color:var(--green-text)}
.call-photo{position:absolute;left:776px;top:184px;width:258px;height:124px;
  background:radial-gradient(ellipse 40% 55% at 45% 40%,#e9d4c4 0%,#d5b8a4 40%,transparent 70%),linear-gradient(180deg,#fafafa 0%,#6a6a6a 55%,#2a2a2a 100%);
  -webkit-mask-image:radial-gradient(ellipse 75% 100% at 50% 100%,#000 70%,transparent);mask-image:radial-gradient(ellipse 75% 100% at 50% 100%,#000 70%,transparent)}
.call-box{position:absolute;left:768px;top:305px;width:282px;height:200px;background:var(--cream);box-shadow:0 4px 8px rgba(0,0,0,.15);text-align:center;color:var(--green-deep)}
.call-title{font-size:26px;margin-top:12px}
.call-number{font-size:36px;color:var(--red);margin-top:0;letter-spacing:.5px}
.call-sub{font-size:15.5px;line-height:17px;margin-top:4px}
.call-input{position:absolute;left:8px;top:131px;width:176px;height:27px;background:#fff;border:1px solid #d6d0b0;border-radius:3px}
.call-btn{position:absolute;left:193px;top:131px;width:74px;height:27px;background:linear-gradient(#9fd44a,#5fa820);border-radius:3px;color:#fff;font-size:16px;line-height:27px}
.call-email{position:absolute;left:0;top:172px;width:282px;font-size:14px;color:#555}
.call-arrow{position:absolute;left:1004px;top:472px}
.feature{position:absolute;top:551px;width:279px;height:87px;border-radius:6px;background:linear-gradient(180deg,#b5df4c,#72b52a);border:1px solid #9ccc55;overflow:hidden;font-family:"Roboto Condensed","Arial Narrow",sans-serif;color:#1e4a08}
.feature-photo{position:absolute;left:0;top:0;width:100px;height:87px;background:linear-gradient(160deg,#c9c4bf 0%,#e3a77e 50%,#8a8e90 100%)}
.feature h2{position:absolute;left:103px;top:7px;font-size:27px;font-weight:400;letter-spacing:-.3px}
.feature p{position:absolute;left:110px;top:44px;font-size:17px;line-height:17px}
.feature p.one{top:50px}
.feature svg{position:absolute;right:13px;top:30px}
.footer-rule{position:absolute;left:0;top:658px;width:1200px;height:3px;background:var(--lime-dark)}
.footer{position:absolute;left:0;top:661px;width:1200px;height:118px;background:linear-gradient(180deg,#9bcd3b,#c6e45e 50%,#a7d441)}
.copy{position:absolute;left:178px;top:10px;font-size:12px;color:#fff}
.foot-links{position:absolute;left:176px;top:33px;font-size:12px;color:#fff}
.select{position:absolute;left:535px;top:15px;width:217px;height:25px;background:var(--cream);border:1px solid #c9c39a;font-size:12px;color:#444;padding:6px 9px}
.select svg{position:absolute;right:3px;top:6px}
.social{position:absolute;left:898px;top:16px;display:flex;gap:9px}
.social span{width:28px;height:28px;border-radius:4px;background:var(--green-deep)}
</style>
</head>
<body>
<div class="top-band"></div>
<header class="header"></header>
<div class="brand"><span class="brand-mark"></span><span class="brand-name">CORNER CASH POINT</span></div>
<div class="search"><svg width="16" height="16"><polygon points="2,1 15,8 2,15" fill="#6cb51f"/></svg>Search Site</div>
<svg class="search-btn" width="26" height="26"><circle cx="10" cy="10" r="7.5" fill="none" stroke="#777" stroke-width="2"/><line x1="15.5" y1="15.5" x2="24" y2="24" stroke="#555" stroke-width="3" stroke-linecap="round"/></svg>
<ul class="nav">
  <li class="active" style="left:169px">HOME</li>
  <li style="left:237px">ABOUT CCP</li>
  <li style="left:337px">INVESTORS</li>
  <li style="left:422px">PRODUCTS AND SERVICES</li>
  <li style="left:591px">GET A FREE ATM</li>
  <li style="left:701px">GIVING BACK</li>
  <li style="left:793px">WHO HAS ONE</li>
  <li style="left:900px">MEDIA</li>
  <li style="left:961px">CARRERS</li>
</ul>
<div class="nav-rule"></div>
<main class="main"></main>
<div class="atm-art" role="img" aria-label="Green branded ATM machine"></div>
<p class="hero-text">At CORNER CASH POINT unlike the bank's is proud to give back money to the store owner and the com-munity from every transaction.</p>
<div class="call-photo" role="img" aria-label="Smiling businesswoman leaning on the call box"></div>
<section class="call-box">
  <div class="call-title">Questions? Call Now!</div>
  <div class="call-number">1300 482 731</div>
  <div class="call-sub">or enter your phone number and<br>we will call you</div>
  <div class="call-input"></div>
  <div class="call-btn">Call Me</div>
  <div class="call-email">or email us: info@ccpoint.com</div>
</section>
<svg class="call-arrow" width="52" height="78"><path d="M6 74 C40 62 48 38 36 14" fill="none" stroke="#6cb51f" stroke-width="5"/><polygon points="24,18 36,2 46,20" fill="#6cb51f"/></svg>
<a class="feature" style="left:169px"><div class="feature-photo" role="img" aria-label="Hand using an ATM keypad"></div><h2>Get an ATM</h2><p class="one">for your business</p><svg width="28" height="28"><circle cx="14" cy="14" r="13" fill="#fff"/><path d="M11 8 L17 14 L11 20" fill="none" stroke="#6cb51f" stroke-width="3"/></svg></a>
<a class="feature" style="left:470px"><div class="feature-photo" role="img" aria-label="Hand using an ATM keypad"></div><h2>Own an ATM</h2><p>Increase your<br>investment Portfolio</p><svg width="28" height="28"><circle cx="14" cy="14" r="13" fill="#fff"/><path d="M11 8 L17 14 L11 20" fill="none" stroke="#6cb51f" stroke-width="3"/></svg></a>
<a class="feature" style="left:769px"><div class="feature-photo" role="img" aria-label="Hand using an ATM keypad"></div><h2>Latest ATM</h2><p>See an ATM<br>in action</p><svg width="28" height="28"><circle cx="14" cy="14" r="13" fill="#fff"/><path d="M11 8 L17 14 L11 20" fill="none" stroke="#6cb51f" stroke-width="3"/></svg></a>
<div class="footer-rule"></div>
<footer class="footer">
  <div class="copy">Copyright © 2010 &nbsp;CCP</div>
  <div class="foot-links">Search Privacy &nbsp;•&nbsp; Terms of use &nbsp;•&nbsp; Site map</div>
  <div class="select">Get an ATM from<svg width="14" height="12"><rect width="14" height="12" fill="#ddd"/><path d="M3 4 L7 8 L11 4" fill="none" stroke="#555" stroke-width="2"/></svg></div>
  <div class="social" aria-label="Social links"><span></span><span></span><span></span><span></span></div>
</footer>
</body>
</html>
```